Brightwell Giving Inc

We need a full re-design of our non-profit organization website (www.brightwellgiving.org). Ideally, we are looking to make it more attractive, user-friendly, and interactive with our business model.

Please make sure to user colors that ago with our logo.

We need a homepage done and we also need a content page done where we will use for the other pages to fill with content.

Target Market(s)

Clothes/textiles donations.

Industry/Entity Type

Charity

Number of Pages Required

2 page

Colors

Designer to choose colors to be used in the design.

Requirements
Must have
• It must match the styling of our logo and same colors as current website. (www.brightwellgiving.org)
Nice to have
• Sleek homepage that is easy to understand and get our main points across.

```html
<!DOCTYPE html>
<html lang="en">
<head>
<meta charset="utf-8">
<title>Brightwell Giving — Home</title>
<link rel="stylesheet" href="https://fonts.googleapis.com/css2?family=Roboto:wght@400;500;700;900&family=Roboto+Condensed:wght@700&display=swap">
<style>
:root{
  --yellow:#fcd629;
  --yellow-btn:#f6c900;
  --ink:#1c1c1c;
  --text:#2b2b2b;
  --muted:#555;
  --topbar:#161616;
  --green:#3d8b2f;
  --white:#fff;
  --line:#e2e2e2;
  --slate:#4a5d68;
}
*{box-sizing:border-box;margin:0;padding:0}
html,body{width:1200px;height:2703px;overflow:hidden}
body{font-family:"Roboto",Arial,sans-serif;color:var(--text);background:var(--white);position:relative}
section,header,footer,.topbar{position:absolute;left:0;width:1200px}

.topbar{top:0;height:34px;background:var(--topbar);color:var(--white);font-size:11px;font-weight:700}
.topbar .phone{position:absolute;top:11px;white-space:nowrap}
.topbar .search{position:absolute;left:878px;top:4px;width:194px;height:26px;background:#3b3b3b;border-radius:3px;color:#ddd;font-weight:400;font-size:11px;padding:7px 10px;white-space:nowrap}
.topbar .search svg{position:absolute;right:8px;top:6px}

.site-header{top:34px;height:85px;background:var(--white);border-bottom:1px solid var(--line)}
.brand{position:absolute;left:122px;top:26px;display:flex;align-items:center;gap:10px}
.brand-mark{width:32px;height:32px;background:var(--green);flex:none}
.brand-name{font-size:24px;font-weight:700;color:var(--green);white-space:nowrap}
.nav{position:absolute;left:0;top:37px;width:1200px;height:14px;font-size:11px;font-weight:700;color:var(--ink)}
.nav span{position:absolute;top:0;white-space:nowrap}
.donate{position:absolute;left:1007px;top:29px;width:64px;height:30px;background:var(--yellow-btn);font-size:11px;font-weight:700;text-align:center;line-height:30px;border-radius:2px}

.hero{top:119px;height:483px;background:linear-gradient(100deg,#4a3a2c 0%,#6b5341 35%,#3e2c22 60%,#7a6553 100%)}
.hero h1{position:absolute;left:122px;top:160px;font-family:"Roboto Condensed","Roboto",sans-serif;font-size:44px;line-height:50px;color:var(--white);text-transform:uppercase;white-space:nowrap}
.btn-learn{position:absolute;left:124px;top:281px;width:164px;height:37px;background:var(--yellow-btn);color:var(--ink);font-size:13px;font-weight:700;text-align:center;line-height:37px;border-radius:3px}
.dots{position:absolute;left:124px;top:448px;display:flex;gap:6px}
.dots i{width:13px;height:13px;border-radius:50%;border:2px solid var(--white);display:block}
.dots i.on{background:var(--yellow-btn);border-color:var(--yellow-btn)}

.who{top:602px;height:331px;background:var(--yellow);text-align:center}
.who h2{margin-top:62px;font-size:33px;font-weight:900;color:var(--ink)}
.who .rule{width:108px;height:2px;background:var(--ink);margin:14px auto 0}
.who p{width:720px;margin:26px auto 0;font-size:11.5px;line-height:20px;color:var(--ink)}
.pointer{position:absolute;left:578px;top:933px;width:0;height:0;border-left:22px solid transparent;border-right:22px solid transparent;border-top:22px solid var(--yellow)}

.section-title{position:absolute;left:122px;font-size:25px;font-weight:700;color:var(--yellow-btn)}
.mission{top:955px;height:409px}
.mission .section-title{top:50px}
.mission-card{position:absolute;top:99px;width:299px}
.mission-card .photo{height:173px}
.mission-card h3{margin-top:14px;font-size:16px;font-weight:500;line-height:21px;color:var(--ink);text-transform:uppercase;padding-left:7px}

.how{top:1364px;height:447px;background:linear-gradient(90deg,#7a6a55 0%,#9a8a72 30%,#5c4e40 70%,#8a6f5c 100%)}
.how h2{position:absolute;top:62px;width:1200px;text-align:center;font-size:31px;font-weight:700;color:var(--white)}
.step{position:absolute;top:173px;width:314px;height:180px;background:rgba(255,255,255,.92);text-align:center;padding:17px 26px 0}
.step .num{position:absolute;left:117px;top:-36px;width:80px;height:80px;border-radius:50%;background:rgba(255,255,255,.92);color:var(--yellow-btn);font-size:25px;font-weight:700;padding-top:14px}
.step h3{position:relative;font-size:16px;font-weight:500;line-height:21px;color:var(--ink)}
.step .rule{width:36px;height:2px;background:var(--ink);margin:14px auto 12px}
.step p{font-size:11.5px;line-height:19px;color:var(--text)}

.news{top:1811px;height:549px}
.news .section-title{top:52px}
.feature{position:absolute;left:122px;top:101px;width:467px}
.feature .thumb{height:258px;border:1px solid var(--line);display:flex;align-items:center;justify-content:center;gap:14px}
.thumb-name{font-weight:700;color:var(--ink);white-space:nowrap}
.date{position:absolute;left:0;top:0;background:var(--yellow-btn);color:var(--ink);text-align:center;font-weight:900;line-height:1}
.feature .date{width:56px;height:56px;padding-top:8px;font-size:24px}
.date small{display:block;font-size:10px;font-weight:700;margin-top:2px;text-transform:uppercase}
.feature h3{margin-top:22px;font-size:16px;font-weight:500;padding-left:8px;color:var(--ink)}
.feature p{margin-top:10px;font-size:11px;line-height:18px;padding-left:8px;color:var(--text)}
.read-more{display:block;font-size:11px;font-weight:500;color:var(--yellow-btn);text-transform:uppercase}
.feature .read-more{margin-top:16px;padding-left:8px}
.news-item{position:absolute;left:605px;width:500px;height:108px}
.news-item .thumb{position:absolute;left:0;top:0;width:157px;height:106px;border:1px solid var(--line);display:flex;align-items:flex-end;justify-content:center;padding-bottom:12px;font-size:12px}
.news-item .date{width:46px;height:46px;padding-top:6px;font-size:21px}
.news-item .body{position:absolute;left:172px;top:2px;width:320px}
.news-item h4{font-size:16px;font-weight:500;color:var(--ink);white-space:nowrap}
.news-item p{margin-top:9px;font-size:11px;line-height:18px;color:var(--text)}
.news-item .read-more{margin-top:9px}

.map-widget{top:2360px;height:289px}
.map-bar{height:36px;background:var(--slate);color:var(--white);font-size:14px;font-weight:500;padding:10px 0 0 48px;position:relative}
.map-bar .ico{position:absolute;left:12px;top:11px;width:16px;height:14px;border:2px solid var(--white)}
.map-bar .tools{position:absolute;right:14px;top:10px;display:flex;gap:14px}
.map-area{height:253px;background:linear-gradient(135deg,#e9e4d6 0%,#dfe3cf 40%,#e6e0d0 70%,#dcdccc 100%)}

.site-footer{top:2649px;height:54px;background:var(--topbar);color:#cfcfcf;font-size:10px;font-weight:500}
.site-footer .copy{position:absolute;left:122px;top:21px;letter-spacing:.3px}
.site-footer .social{position:absolute;left:1048px;top:15px;width:22px;height:22px;background:#e6e6e6;border-radius:3px}
</style>
</head>
<body>

<div class="topbar">
  <span class="phone" style="left:124px">TOLL FREE: (855) 555-0142</span>
  <span class="phone" style="left:284px">NEW YORK: 518-555-0176</span>
  <div class="search">Find Local Donation Place : Zip
    <svg width="14" height="14" viewBox="0 0 14 14"><circle cx="6" cy="6" r="4.5" fill="none" stroke="#fff" stroke-width="2"/><line x1="9.5" y1="9.5" x2="13" y2="13" stroke="#fff" stroke-width="2"/></svg>
  </div>
</div>

<header class="site-header">
  <div class="brand"><span class="brand-mark"></span><span class="brand-name">Brightwell Giving</span></div>
  <nav class="nav">
    <span style="left:505px">MISSION</span>
    <span style="left:574px">HOW IT WORKS</span>
    <span style="left:679px">ABOUT US</span>
    <span style="left:758px">SPONSORS</span>
    <span style="left:843px">NEWS</span>
    <span style="left:901px">WALL OF NEEDS</span>
  </nav>
  <div class="donate">DONATE</div>
</header>

<section class="hero" role="img" aria-label="Photo of smiling children looking at the camera">
  <h1>Think Globally While<br>Donating Locally</h1>
  <div class="btn-learn">LEARN MORE</div>
  <div class="dots"><i class="on"></i><i></i><i></i><i></i></div>
</section>

<section class="who">
  <h2>WHO WE ARE</h2>
  <div class="rule"></div>
  <p>Brightwell Giving is a non-profit organization that was created for one purpose: helping the less fortunate in our country's time of greatest need. Started in 2007, Brightwell Giving has been a dedicated member of its local communities over the past four years. The company's clothing collection efforts have allowed it to provide some of the neediest members of the community to clothe themselves and their families. The company's goal is to ensure that some of the most basic needs of the community's members are met through the philanthropic efforts of the organizations members and contributors.</p>
</section>
<div class="pointer"></div>

<section class="mission">
  <h2 class="section-title">Our Mission</h2>
  <div class="mission-card" style="left:122px">
    <div class="photo" role="img" aria-label="Photo of protest signs against gun violence in schools" style="background:linear-gradient(90deg,#c9c2c0,#d4c9d8)"></div>
    <h3>Support Anti-Gun Violence</h3>
  </div>
  <div class="mission-card" style="left:449px">
    <div class="photo" role="img" aria-label="Photo of people wading through a flooded street" style="background:linear-gradient(180deg,#8d9086,#a8a89c)"></div>
    <h3>Help Disaster Victims of<br>Hurrican Irene</h3>
  </div>
  <div class="mission-card" style="left:775px">
    <div class="photo" role="img" aria-label="Photo of a green clothing donation bin in a parking lot" style="background:linear-gradient(180deg,#9fa3a0,#4fa04a 55%,#8e8e88)"></div>
    <h3>Help Hudson Family Alliance</h3>
  </div>
</section>

<section class="how" role="img" aria-label="Blurred photo of a volunteer sorting donated clothing on racks">
  <h2>How It Works?</h2>
  <div class="step" style="left:122px">
    <div class="num">01</div>
    <h3>Drop off clothing at your closest donation bin</h3>
    <div class="rule"></div>
    <p>We have different collection procedures. For outdoors we can place a donation bin, Inside collecting we would use a commercial laundry bin.</p>
  </div>
  <div class="step" style="left:441px">
    <div class="num">02</div>
    <h3>We pick it up and take it to our sorting facility</h3>
    <div class="rule"></div>
    <p>After our drivers pick up the clothing from our designated donation locations, the items are taken to our sorting facility where they are separated into three categories.</p>
  </div>
  <div class="step" style="left:762px">
    <div class="num">03</div>
    <h3>Charities get clothing. We pay you for the clothes</h3>
    <div class="rule"></div>
    <p>Once we are done distributing our donated clothing to their appropriate channels, the proceeds from the sales are distributed in two ways.</p>
  </div>
</section>

<section class="news">
  <h2 class="section-title">Latest News</h2>
  <article class="feature">
    <div class="thumb"><span class="brand-mark" style="width:44px;height:44px"></span><span class="thumb-name" style="font-size:34px">Brightwell Giving</span></div>
    <div class="date">16<small>May</small></div>
    <h3>Charity Project Love Thy Neighbor-Elena</h3>
    <p>04/15/2017. Started Charitable project LOVE THY NEIGHBOR-ELENA. Brightwell Giving team starts to install donation boxes and collect money to help Elena. She was born with a difficult genetic disorder Chromosomal pathology-deletion long...</p>
    <span class="read-more">Read More</span>
  </article>

  <article class="news-item" style="top:101px">
    <div class="thumb"><span class="thumb-name">Brightwell Giving</span></div>
    <div class="date">12<small>Apr</small></div>
    <div class="body">
      <h4>Brightwell Giving ShopRow store</h4>
      <p>April 4, 2017: Brightwell Giving started its own ShopRow store to sell clothes. Brightwell Giving started its...</p>
      <span class="read-more">Read More</span>
    </div>
  </article>
  <article class="news-item" style="top:225px">
    <div class="thumb"><span class="thumb-name">Brightwell Giving</span></div>
    <div class="date">19<small>Feb</small></div>
    <div class="body">
      <h4>We are proud to announce Brightwell...</h4>
      <p>We are proud to announce Brightwell Giving Inc has been interviewed by Dana Kessler, a reporter from...</p>
      <span class="read-more">Read More</span>
    </div>
  </article>
  <article class="news-item" style="top:348px">
    <div class="thumb"><span class="thumb-name">Brightwell Giving</span></div>
    <div class="date">19<small>Feb</small></div>
    <div class="body">
      <h4>At Brightwell Giving</h4>
      <p>At Brightwell Giving we are currently in the process of finalizing a couple of new programs. We will be...</p>
      <span class="read-more">Read More</span>
    </div>
  </article>
</section>

<section class="map-widget">
  <div class="map-bar"><span class="ico"></span>Brightwell Giving...
    <div class="tools">
      <svg width="14" height="14" viewBox="0 0 14 14"><circle cx="3" cy="7" r="2" fill="#fff"/><circle cx="11" cy="3" r="2" fill="#fff"/><circle cx="11" cy="11" r="2" fill="#fff"/><path d="M3 7L11 3M3 7l8 4" stroke="#fff" stroke-width="1.4"/></svg>
      <svg width="14" height="14" viewBox="0 0 14 14" fill="none" stroke="#fff" stroke-width="1.6"><path d="M1 5V1h4M9 1h4v4M13 9v4H9M5 13H1V9"/></svg>
    </div>
  </div>
  <div class="map-area" role="img" aria-label="Road map of upstate New York and western New England marked with donation bin locations"></div>
</section>

<footer class="site-footer">
  <span class="copy">© 2018 BRIGHTWELL GIVING. ALL RIGHTS RESERVED.</span>
  <span class="social"></span>
</footer>

</body>
</html>
```